Ronan Pike Building Business Card Design

Hi,

I need a business card for my Building company.
I am a Builder and build homes for clients.
I am looking for a sophisticated logo that can be used on business cards, envelopes and letter heads.
I am trying to take my business to the next level and need a professional business card.

Colours: Please use white, black, dark grey and bright blue.

Thank you,

Marnie and Ronan.

Target Market(s)

1. Home and Building Companies 2. Potential customers

Industry/Entity Type

Business

Contact Information for Business Card

Ronan Pike Building PTY LTD

Ronan Pike

Director

A.B.N. 37 902 518 617

BUILDERS LICENCE No. 573019k

Mobile: 0471 283 906

Email: ronanpikebuilding@maildrop-example.com.au

Requirements
Must have
• The following is compulsory to have in the designs:

Ronan Pike Building PTY LTD (business name)

Ronan Pike (contact name)

Director (position)

A.B.N. 37 902 518 617

Builders Licence No. 573019k

Mobile: 0471 283 906

Nice to have
• Logo for business
Should not have
• Should not be cluttered.

I am looking for a clean, sophisticated and professional business card design.

```html
<!DOCTYPE html>
<html lang="en">
<head>
<meta charset="utf-8">
<title>Ronan Pike Building – Business Cards</title>
<link href="https://fonts.googleapis.com/css2?family=Roboto+Slab:wght@400;500&family=Roboto+Condensed:wght@400;500&display=swap" rel="stylesheet">
<style>
  :root {
    --stage: #939598;
    --card: #000000;
    --blue: #1aa7e0;
    --grey: #6d6e71;
    --white: #ffffff;
  }
  * { margin: 0; padding: 0; box-sizing: border-box; }
  html, body { width: 1200px; height: 826px; overflow: hidden; background: var(--stage); }
  .stage { position: relative; width: 1200px; height: 826px; }

  .card {
    position: absolute;
    width: 516px;
    height: 286px;
    overflow: hidden;
    background: var(--card);
    color: var(--white);
    font-family: "Roboto Slab", Georgia, serif;
  }
  .card--front-grey { left: 74px; top: 96px; }
  .card--back-grey  { left: 74px; top: 392px; }
  .card--front-blue { left: 618px; top: 101px; }
  .card--back-blue  { left: 618px; top: 397px; }

  .brand { position: absolute; display: flex; align-items: center; }
  .brand__square { background: var(--blue); flex: none; }
  .brand__name {
    font-family: "Roboto Slab", Georgia, serif;
    font-weight: 500;
    line-height: 1.02;
    white-space: nowrap;
  }
  .brand__suffix { font-size: 0.26em; vertical-align: 1.6em; margin-left: 3px; letter-spacing: 0.3px; }
  .brand--grey .brand__name { color: var(--grey); }
  .brand--blue .brand__name { color: var(--blue); }

  .brand--small { left: 36px; top: 54px; gap: 14px; }
  .brand--small .brand__square { width: 46px; height: 46px; }
  .brand--small .brand__name { font-size: 25px; }

  .card--front-blue .brand--small { top: 42px; }
  .card--front-blue .brand--small .brand__name { font-size: 28px; }
  .card--front-blue .brand--small .brand__square { width: 52px; height: 52px; }

  .brand--large { left: 100px; top: 96px; gap: 18px; }
  .brand--large .brand__square { width: 84px; height: 84px; }
  .brand--large .brand__name { font-size: 36px; }

  .brand--medium { left: 118px; top: 100px; gap: 16px; }
  .brand--medium .brand__square { width: 70px; height: 70px; }
  .brand--medium .brand__name { font-size: 31px; }

  .line { position: absolute; white-space: nowrap; }
  .role, .legal { font-size: 12px; letter-spacing: 0.2px; }
  .person { font-size: 21px; font-weight: 500; }
  .contact {
    font-family: "Roboto Condensed", "Arial Narrow", sans-serif;
    font-weight: 500;
    font-size: 15px;
  }
  .contact--email { font-size: 12.5px; letter-spacing: -0.1px; }
  .contact__label { color: var(--blue); margin-right: 4px; }

  .divider { position: absolute; width: 2px; background: var(--blue); }
</style>
</head>
<body>
<main class="stage">

  <section class="card card--front-grey">
    <div class="brand brand--grey brand--small">
      <span class="brand__square"></span>
      <span class="brand__name">Ronan Pike<br>Building<span class="brand__suffix">PTY LTD</span></span>
    </div>
    <p class="line role" style="left:32px; top:182px;">Director</p>
    <p class="line legal" style="left:32px; top:217px;">A.B.N. 37 902 518 617</p>
    <p class="line legal" style="left:32px; top:238px;">BUILDERS LICENCE No. 573019k</p>
    <span class="divider" style="left:248px; top:205px; height:62px;"></span>
    <p class="line person" style="left:260px; top:172px;">Ronan Pike</p>
    <p class="line contact" style="left:260px; top:213px;"><span class="contact__label">M:</span>0471 283 906</p>
    <p class="line contact contact--email" style="left:260px; top:237px;"><span class="contact__label">E:</span>ronanpikebuilding@maildrop-example.com.au</p>
  </section>

  <section class="card card--back-grey">
    <div class="brand brand--grey brand--large">
      <span class="brand__square"></span>
      <span class="brand__name">Ronan Pike<br>Building<span class="brand__suffix">PTY LTD</span></span>
    </div>
  </section>

  <section class="card card--front-blue">
    <div class="brand brand--blue brand--small">
      <span class="brand__square"></span>
      <span class="brand__name">Ronan Pike<br>Building<span class="brand__suffix">PTY LTD</span></span>
    </div>
    <p class="line person" style="left:36px; top:172px;">Ronan Pike</p>
    <p class="line contact" style="left:34px; top:213px;"><span class="contact__label">M:</span>0471 283 906</p>
    <p class="line contact contact--email" style="left:34px; top:237px;"><span class="contact__label">E:</span>ronanpikebuilding@maildrop-example.com.au</p>
    <span class="divider" style="left:300px; top:210px; height:42px;"></span>
    <p class="line role" style="left:312px; top:185px;">Director</p>
    <p class="line legal" style="left:312px; top:219px;">A.B.N. 37 902 518 617</p>
    <p class="line legal" style="left:312px; top:240px;">BUILDERS LICENCE No. 573019k</p>
  </section>

  <section class="card card--back-blue">
    <div class="brand brand--blue brand--medium">
      <span class="brand__square"></span>
      <span class="brand__name">Ronan Pike<br>Building<span class="brand__suffix">PTY LTD</span></span>
    </div>
  </section>

</main>
</body>
</html>
```